The most amazing design opportunity you will ever get - Plus we may even through in some shares!

We need a new look and feel for our website, something that will knock the socks off our competitors. Something fresh, functional, dynamic and awesome.

Take a look at the attached brief and see if this is something you can get you head around to come up with something just amazing.

Reason: need more designs

A key to your success is to base your design on the Visual Language (colours Black with Orange on white background, integration of cogs, font, style) and remember that our target audience is BUSINESS and the key thing that we are about is INSIGHTS, so if you can include some subtle design that requires insight to use - Perfect!

```html
<!DOCTYPE html>
<html lang="en">
<head>
<meta charset="utf-8">
<title>Keystone Insight — Business Solutions Through Insight</title>
<link rel="stylesheet" href="https://fonts.googleapis.com/css2?family=Open+Sans:wght@400;600;700&display=swap">
<style>
:root{
  --orange:#f28a1f;
  --orange-dark:#e07512;
  --ink:#222222;
  --text:#555555;
  --muted:#8a8a8a;
  --bar:#1d1d1d;
  --tabbar:#474747;
  --nav:#2f2f2f;
  --menu:#3a3a3a;
  --panel:#e4e4e4;
  --footer:#2b2b2b;
  --footer-bottom:#1f1f1f;
  --footer-link:#a0a0a0;
  --t1:#a2cb16;--t2:#38b47a;--t3:#1ba0b8;--t4:#6253a6;--t5:#2c7fd2;--t6:#a35ddf;--t7:#18a656;
}
*{box-sizing:border-box;margin:0;padding:0}
html,body{width:1200px;height:2219px;overflow:hidden}
body{position:relative;background:#fff;font-family:"Open Sans",Arial,sans-serif;color:var(--text)}
.abs{position:absolute}

/* stats bar */
.stats{left:0;top:0;width:1200px;height:98px;background:linear-gradient(#2a2a2a,#111)}
.stat{position:absolute;top:8px;width:143px;height:82px;display:flex;align-items:center;padding-left:12px;color:#fff;gap:9px;overflow:hidden}
.stat svg{width:26px;height:26px;flex:none}
.stat div{min-width:0;white-space:nowrap}
.stat b{display:block;font-weight:400;font-size:18px;line-height:21px;letter-spacing:-.2px}
.stat span{font-size:13px;line-height:15px}
.stat.active{outline:2px solid #fff;outline-offset:-2px}

/* audience tabs */
.audience{left:0;top:98px;width:1200px;height:40px;background:var(--tabbar);border-bottom:1px solid #2e2e2e}
.audience a{position:absolute;top:0;height:40px;line-height:40px;text-align:center;color:#fff;font-size:15px;text-decoration:none;border-left:1px solid #5a5a5a}
.audience a.on{background:var(--orange);border:none}

/* header */
.brand{left:100px;top:180px;display:flex;align-items:center;gap:16px}
.brand-mark{width:46px;height:46px;border-radius:50%;background:var(--orange)}
.brand-name{font-size:40px;font-weight:700;color:var(--ink);line-height:1}
.brand-tag{font-size:17px;line-height:20px;color:var(--ink);margin-left:6px}

.notice{left:647px;top:160px;width:453px;height:115px;border:2px solid #bdbdbd;background:#fff}
.notice .row{height:19px;line-height:19px;font-size:11px;color:#fff;font-weight:700;padding-left:18px;background:#3a3a3a;border-bottom:1px solid #222;position:relative}
.notice .row::after{content:"";position:absolute;right:6px;top:5px;width:5px;height:9px;background:#ddd}
.notice .row.promo{background:var(--orange)}
.promo-item{height:22px;display:flex;align-items:center;font-size:10px;color:#777;padding-left:14px;gap:6px;white-space:nowrap}
.promo-item i{width:14px;height:14px;background:#b49a84;display:block}
.promo-item .who{color:var(--orange);width:100px;font-style:normal}
.promo-item .rank{color:#333;font-weight:700;width:24px;text-align:right}
.promo-item .stars{color:#f3b21c;letter-spacing:1px}
.promo-item .rate{background:var(--orange);color:#fff;font-size:9px;padding:1px 8px;margin-left:10px}
.promo-item .rate.off{background:#aaa}

/* main nav */
.mainnav{left:100px;top:296px;width:1000px;height:46px;background:var(--nav)}
.mainnav a{position:absolute;top:0;height:46px;line-height:46px;color:#fff;font-weight:700;font-size:15px;text-decoration:none;text-align:center}
.mainnav a.on{background:var(--orange);width:163px;left:0}
.mainnav a.on::after{content:"";position:absolute;left:74px;bottom:-8px;border:8px solid transparent;border-top-color:var(--orange);border-bottom:0}

.hero{left:100px;top:342px;width:1000px;height:417px;background:radial-gradient(circle at 60% 35%,#f25a2a 0,#f59a2a 22%,transparent 45%),radial-gradient(circle at 20% 55%,#9a4fd8 0,#2aa4e0 20%,transparent 42%),radial-gradient(circle at 90% 55%,#8cc63f 0,#2db36a 18%,transparent 38%),radial-gradient(circle at 45% 70%,#e6336f 0,transparent 30%),linear-gradient(#fff,#fbe9d8)}
.dropdown{left:100px;top:357px;width:169px;list-style:none}
.dropdown li{height:39px;line-height:38px;padding-left:20px;background:var(--menu);border-bottom:1px solid #232323;color:#fff;font-size:15px}
.dropdown li.on{background:linear-gradient(#f39a35,var(--orange-dark))}
.dots{left:572px;top:779px;display:flex;gap:6px}
.dots i{width:6px;height:6px;border-radius:50%;background:#ccc}
.dots i:first-child{background:var(--orange)}

/* why section */
.section-title{font-size:18px;font-weight:700;color:var(--orange);text-transform:uppercase}
.video{left:100px;top:863px;width:297px;height:234px;background:linear-gradient(#1b1b1b 0,#2a2a2a 18%,#e9eef3 18%,#cfd9e4 70%,#1e5f8f 100%)}
.play{left:228px;top:953px;width:46px;height:46px;border:3px solid #fff;border-radius:50%;background:rgba(0,0,0,.35)}
.play::after{content:"";position:absolute;left:15px;top:10px;border:10px solid transparent;border-left:14px solid #fff;border-right:0}
.intro{left:422px;top:862px;width:256px;font-size:12px;line-height:16.2px;text-align:justify;color:#777}

.auth{left:709px;top:817px;width:391px;height:280px;background:var(--panel)}
.auth-tabs{height:46px;background:#fff;display:flex}
.auth-tabs span{width:73px;text-align:center;line-height:46px;font-size:16px;color:#777}
.auth-tabs span.on{background:var(--panel);color:#333;font-weight:600}
.field{position:absolute;left:39px;width:316px;height:37px;background:#fff;border:1px solid #d3d3d3;font-size:13px;color:#bbb;padding-left:18px;line-height:35px}
.auth .btn{position:absolute;left:216px;top:197px;width:140px;height:33px;background:var(--orange);color:#fff;text-align:center;line-height:33px;font-size:15px;border:1px solid #d66f0c}
.forgot{position:absolute;left:230px;top:241px;font-size:12px;color:#999}

/* live feed */
.arrows{display:flex;gap:7px}
.arrows i{width:18px;height:18px;border-radius:50%;background:#8c8c8c;position:relative}
.arrows i.on{background:var(--orange)}
.arrows i::after{content:"";position:absolute;left:5px;top:5px;width:6px;height:6px;border-left:2px solid #fff;border-bottom:2px solid #fff;transform:translateX(2px) rotate(45deg)}
.arrows i.next::after{transform:translateX(-1px) rotate(-135deg)}
.card{position:absolute;top:1211px;width:238px}
.card .pic{height:152px;border:1px solid #ddd}
.card h3{margin-top:20px;font-size:13px;font-weight:600;color:#222;line-height:19px;text-transform:uppercase}
.card p{font-size:12px;color:#555;line-height:18px}
.card time{display:block;font-size:9px;color:#999;font-weight:700;margin-top:3px}
.rule{left:0;top:1539px;width:1200px;height:1px;background:#d6d6d6}
.banner{position:absolute;top:1585px;width:240px;height:107px;border:1px solid #ddd}

/* footer */
.footer{left:0;top:1751px;width:1200px;height:388px;background:var(--footer)}
.fcol{position:absolute;top:1814px}
.fcol h4{font-size:16px;font-weight:400;color:var(--orange);margin-bottom:8px;line-height:20px}
.fcol ul{list-style:none}
.fcol li{font-size:13px;color:var(--footer-link);line-height:26px;white-space:nowrap}
.fbottom{left:0;top:2139px;width:1200px;height:80px;background:var(--footer-bottom)}
.legal{left:100px;top:2158px;font-size:11px;color:#777;line-height:20px}
.legal span{margin-right:10px}
.social{left:942px;top:2165px;display:flex;gap:13px}
.social i{width:30px;height:30px;border-radius:50%;background:#fff}
</style>
</head>
<body>

<div class="abs stats">
  <div class="stat active" style="left:100px;background:var(--t1)"><svg viewBox="0 0 30 30"><circle cx="15" cy="9" r="6" fill="#fff"/><path d="M3 28c0-7 5-11 12-11s12 4 12 11z" fill="#fff"/></svg><div><b>3,458</b><span>iMembers</span></div></div>
  <div class="stat" style="left:243px;background:var(--t2)"><svg viewBox="0 0 30 30"><rect x="6" y="3" width="3" height="25" fill="#fff"/><path d="M9 4h16l-5 5 5 5H9z" fill="#fff"/></svg><div><b>1,700,250</b><span>iPoints</span></div></div>
  <div class="stat" style="left:386px;background:var(--t3)"><svg viewBox="0 0 30 30"><circle cx="15" cy="15" r="9" fill="none" stroke="#fff" stroke-width="5" stroke-dasharray="4 3"/><circle cx="15" cy="15" r="4" fill="#fff"/></svg><div><b>3,458</b><span>iAttributes</span></div></div>
  <div class="stat" style="left:529px;background:var(--t4)"><svg viewBox="0 0 30 30"><path d="M4 27h23" stroke="#fff" stroke-width="2"/><rect x="7" y="16" width="3" height="10" fill="#fff"/><rect x="13" y="11" width="3" height="15" fill="#fff"/><rect x="19" y="14" width="3" height="12" fill="#fff"/></svg><div><b>3,458</b><span>iActivity</span></div></div>
  <div class="stat" style="left:672px;background:var(--t5)"><svg viewBox="0 0 30 30" fill="none" stroke="#fff" stroke-width="2"><circle cx="15" cy="15" r="11"/><ellipse cx="15" cy="15" rx="5" ry="11"/><path d="M4 15h22M6 9h18M6 21h18"/></svg><div><b>300,025</b><span>iNetworking</span></div></div>
  <div class="stat" style="left:815px;background:var(--t6)"><svg viewBox="0 0 30 30"><text x="8" y="23" font-size="22" font-weight="700" fill="#fff" font-family="Arial">$</text></svg><div><b>i$900,125</b><span>iDollars</span></div></div>
  <div class="stat" style="left:958px;background:var(--t7)"><svg viewBox="0 0 30 30"><path d="M4 11h12V5l10 10-10 10v-6H4z" fill="#fff"/></svg><div><b>900,000</b><span>iShares</span></div></div>
</div>

<nav class="abs audience">
  <a class="on" style="left:100px;width:250px">Everyone</a>
  <a style="left:350px;width:250px">Just me</a>
  <a style="left:600px;width:260px">My Friends</a>
  <a style="left:860px;width:240px">My Teams</a>
</nav>

<div class="abs brand">
  <span class="brand-mark"></span>
  <span class="brand-name">Keystone</span>
  <span class="brand-tag">BUSINESS<br>SOLUTIONS<br>THROUGH<br>INSIGHT</span>
</div>

<aside class="abs notice">
  <div class="row">Did you know?</div>
  <div class="row">New Affiliates</div>
  <div class="row promo">Promotions</div>
  <div class="promo-item"><i></i><em class="who">Dana Whitfield</em>just been promoted to <span class="rank">1st</span> Rank <span class="stars">★★★☆☆</span><span class="rate">Rate it</span></div>
  <div class="promo-item"><i></i><em class="who">Omar Lindqvist</em>just been promoted to <span class="rank">2st</span> Rank <span class="stars">★★★☆☆</span><span class="rate off">Rate it</span></div>
</aside>

<nav class="abs mainnav">
  <a class="on">Insights</a>
  <a style="left:163px;width:163px">Profile</a>
  <a style="left:326px;width:163px">Partner1</a>
  <a style="left:489px;width:163px">Partner2</a>
  <a style="left:652px;width:163px">Partner3</a>
</nav>

<div class="abs hero" role="img" aria-label="Hero illustration of colourful interlocking cogs in blue, purple, red, orange, yellow and green"></div>
<ul class="abs dropdown">
  <li>Disciplines</li><li class="on">Insights</li><li>Library</li><li>Rewards</li><li>Members</li><li>Hire me</li><li>About Us</li>
</ul>
<div class="abs dots"><i></i><i></i><i></i></div>

<h2 class="abs section-title" style="left:100px;top:815px">Why Keystone Insight</h2>
<div class="abs video" role="img" aria-label="Video thumbnail: a 60 second introduction to the portal"></div>
<div class="abs play"></div>
<p class="abs intro">We are dedicated to helping you solve business problems holistically, self-serve or with the help of a specialist. A single portal where you can access solutions and insights across 20 business disciplines. Become a member, share your experi-ences with others, earn points for your participation and get recognized as a trusted advisor in the global community. Start out as a Newbie, then quickly climb the ranks from One Star Intermediate, through to a Five Star Guru.</p>

<div class="abs auth">
  <div class="auth-tabs"><span class="on">Login</span><span style="width:100px">Signup</span></div>
  <div class="field" style="top:83px">User Name</div>
  <div class="field" style="top:133px">Password</div>
  <div class="btn">Password</div>
  <div class="forgot">* Forget Password</div>
</div>

<h2 class="abs section-title" style="left:100px;top:1160px">Live Feed</h2>
<div class="abs arrows" style="left:1056px;top:1166px"><i class="on"></i><i class="next"></i></div>

<article class="card" style="left:100px">
  <div class="pic" role="img" aria-label="Poster-style illustration of a worker flexing her arm" style="background:linear-gradient(135deg,#f2d27a,#c94a2a 55%,#2f4f8f)"></div>
  <h3>Career Development / Crowd-sourcing</h3><p>Women in freelancing event launch</p><time>9 MAY, 2014</time>
</article>
<article class="card" style="left:355px">
  <div class="pic" role="img" aria-label="Grey molecular lattice structure" style="background:linear-gradient(#3a3a3a,#9a9a9a 50%,#5a5a5a)"></div>
  <h3>Creativity and Innovation / Future Ideas / Performance Management</h3><p>Women in freelancing event launch</p><time>9 MAY, 2014</time>
</article>
<article class="card" style="left:609px">
  <div class="pic" role="img" aria-label="Affiliate authors promotional banner with stacked books" style="background:linear-gradient(#fff 0,#fff 45%,#1f63b8 45%)"></div>
  <h3>Business Support</h3><p>Women in freelancing event launch</p><time>9 MAY, 2014</time>
</article>
<article class="card" style="left:863px">
  <div class="pic" role="img" aria-label="Close-up of a printed dictionary entry" style="background:linear-gradient(135deg,#f4f4f4,#cfcfcf)"></div>
  <h3>Crowdsourcing / Knowledge Technology and Culture</h3><p>Women in freelancing event launch</p><time>9 MAY, 2014</time>
</article>

<div class="abs rule"></div>

<div class="abs arrows" style="left:71px;top:1627px"><i class="on"></i></div>
<div class="banner" style="left:100px;background:linear-gradient(#fff 45%,#1f63b8 45%)" role="img" aria-label="Affiliate authors banner"></div>
<div class="banner" style="left:355px;background:linear-gradient(#1f63b8 25%,#fff 25%,#fff 80%,#1f63b8 80%)" role="img" aria-label="Grad school insight companion banner"></div>
<div class="banner" style="left:609px;background:linear-gradient(#fff 55%,#1f63b8 55%)" role="img" aria-label="Insights to employability banner"></div>
<div class="banner" style="left:863px;background:linear-gradient(90deg,#fff 55%,#dfe6ee)" role="img" aria-label="MBAs the ideal insight affiliate banner"></div>
<div class="abs arrows" style="left:1115px;top:1627px"><i class="next"></i></div>

<footer class="abs footer"></footer>
<div class="fcol" style="left:100px"><h4>Disciplines</h4><ul><li>Business Advisory</li><li>Business Analytics</li><li>Business Tools</li><li>Career Development</li><li>Change Management</li><li>Creating Leverage</li><li>Creativity &amp; Innovation</li><li>Crowdsourcing</li></ul></div>
<div class="fcol" style="left:318px;top:1842px"><ul><li>Entrepreneurship</li><li>Future Ideas</li><li>Internet Security</li><li>Knowledge, Technology &amp; Culture</li><li>Leadership</li><li>Marketing</li><li>NLP Success Coaching</li><li>Performance Management</li></ul></div>
<div class="fcol" style="left:597px;top:1842px"><ul><li>Personal Finance &amp; Investments</li><li>Sales</li><li>Social Media</li><li>Strategy</li><li>Systems Thinking</li></ul></div>
<div class="fcol" style="left:869px"><h4>Library</h4><ul><li>Articles</li><li>Books</li><li>Links</li><li>Tutorials</li><li>Videos</li></ul></div>
<div class="fcol" style="left:1001px"><h4>Rewards</h4><ul><li>Insight Points</li><li>Insight Stars</li><li>Insight Dollars</li><li>Insight Affiliates</li></ul></div>

<div class="abs fbottom"></div>
<div class="abs legal"><span>Contact Us</span><span>Privacy &amp; Security</span><span>Terms of Use</span><span>Opt-out</span><br>Copyright 2014 Keystone-Insight.net All Rights Reserved</div>
<div class="abs social" aria-label="Social links"><i></i><i></i><i></i><i></i></div>

</body>
</html>
```